A new novel about the early days of The Quillmarks needs a book cover design

The title of the book is WHEN SPARROWS QUARREL
The cover should also include "a novel" and "by Milo Tavistrand" Those can be together or separate.
The design element I'd like to incorporate is the iconic "Kite Pier" photo of The Quillmarks in 1960, which I've attached below. Since we're not sure if we can get the rights to the actual photo, it's probably best if the design merely references that photo, or distorts it in an interesting way. But it should be very clear that the book is about the Quillmarks.
The novel is in many ways based on that photo and evokes the city of Hamburg in 1960, which was gritty, raw, and sexually charged (as were The Quillmarks).
The tone of the novel is romantic, passionate, and very funny - but never broad and silly.

```html
<!DOCTYPE html>
<html lang="en">
<head>
<meta charset="utf-8">
<title>When Sparrows Quarrel — Cover Wrap</title>
<link rel="stylesheet" href="https://fonts.googleapis.com/css2?family=Bebas+Neue&family=Oswald:wght@500&family=Tinos&display=swap">
<style>
  :root {
    --backdrop: #c3cdcf;
    --red: #cc4a4b;
    --red-deep: #a8302f;
    --cream: #f1e4dc;
    --ink: #2a2626;
    --title-font: "Bebas Neue", "Oswald", sans-serif;
    --label-font: "Oswald", sans-serif;
    --body-font: "Tinos", "Times New Roman", serif;
  }
  * { margin: 0; padding: 0; box-sizing: border-box; }
  html, body { width: 1200px; height: 1066px; overflow: hidden; background: var(--backdrop); }
  .wrap {
    position: absolute; left: 50px; top: 113px;
    width: 1100px; height: 840px;
    display: flex;
    box-shadow: 0 18px 40px rgba(40, 50, 55, 0.25);
  }
  .panel { position: relative; height: 840px; overflow: hidden; background: var(--red); }
  .back-cover, .front-cover { width: 520px; }
  .spine { width: 60px; }
  .panel-art { position: absolute; inset: 0; width: 100%; height: 100%; display: block; }

  .front-title {
    position: absolute; left: 18px; top: 26px;
    font-family: var(--title-font); font-size: 88px; line-height: 0.9;
    color: var(--cream); letter-spacing: 0.5px;
  }
  .front-title .accent { color: var(--ink); }
  .novel-label {
    position: absolute; left: 22px; top: 240px;
    font-family: var(--title-font); font-size: 32px; color: var(--ink);
  }
  .author {
    position: absolute; left: 34px; top: 758px;
    font-family: var(--label-font); font-weight: 500; font-size: 19px;
    letter-spacing: 4px; color: var(--cream);
  }

  .back-title {
    position: absolute; left: 18px; top: 222px;
    font-family: var(--title-font); font-size: 62px; line-height: 0.92;
    color: var(--cream);
  }
  .back-title .accent { color: var(--ink); }
  .blurb {
    position: absolute; left: 20px; top: 360px; width: 300px;
    font-family: var(--body-font); font-size: 12px; line-height: 1.5;
    color: var(--cream); text-align: justify;
  }

  .spine-author, .spine-title {
    position: absolute; left: 0; width: 60px;
    display: flex; justify-content: center;
    writing-mode: vertical-rl; white-space: nowrap;
  }
  .spine-author {
    top: 38px; font-family: var(--label-font); font-weight: 500;
    font-size: 11px; letter-spacing: 2.5px; color: var(--cream);
  }
  .spine-title {
    top: 348px; font-family: var(--title-font); font-size: 28px;
    line-height: 1; color: var(--cream);
  }
  .spine-title .accent { color: var(--red); }
</style>
</head>
<body>
<main class="wrap">

  <section class="panel back-cover">
    <svg class="panel-art" viewBox="0 0 520 840" preserveAspectRatio="none" aria-hidden="true">
      <defs>
        <linearGradient id="backFade" x1="0" y1="0" x2="0" y2="1">
          <stop offset="0" stop-color="#d45a5a"/>
          <stop offset="0.6" stop-color="#cc4a4b"/>
          <stop offset="1" stop-color="#a8302f"/>
        </linearGradient>
      </defs>
      <rect width="520" height="840" fill="url(#backFade)"/>
      <polygon points="0,100 520,200 520,295 0,160" fill="var(--cream)"/>
      <polygon points="0,505 520,590 520,685 0,575" fill="var(--cream)"/>
      <polygon points="405,402 520,395 520,598 480,585 440,560 455,515 420,470" fill="var(--ink)" opacity="0.92"/>
    </svg>
    <h2 class="back-title">When <span class="accent">Sparrows</span><br>Quarrel</h2>
    <p class="blurb">Lorem ipsum dolor sit amet, consectetur adipiscing elit, sed do eiusmod tempor incididunt ut labore et dolore magna aliqua. Ut enim ad minim veniam, quis nostrud exercitation ullamco laboris nisi ut aliquip ex ea commodo consequat. Duis aute irure dolor in reprehenderit in voluptate velit esse cillum dolore eu fugiat nulla pariatur. Excepteur sint occaecat cupidatat non proident, sunt in culpa qui officia deserunt mollit anim id est laborum.</p>
  </section>

  <section class="panel spine">
    <svg class="panel-art" viewBox="0 0 60 840" preserveAspectRatio="none" aria-hidden="true">
      <rect width="60" height="840" fill="var(--red)"/>
      <polygon points="0,200 60,212 60,305 0,295" fill="var(--cream)"/>
      <polygon points="0,590 60,600 60,695 0,685" fill="var(--cream)"/>
      <rect x="0" y="395" width="60" height="200" fill="var(--ink)"/>
    </svg>
    <p class="spine-author">BY MILO TAVISTRAND</p>
    <p class="spine-title"><span>When&nbsp;<span class="accent">Sparrows</span>&nbsp;Quarrel</span></p>
  </section>

  <section class="panel front-cover">
    <svg class="panel-art" viewBox="0 0 520 840" preserveAspectRatio="none">
      <defs>
        <linearGradient id="frontFade" x1="0" y1="0" x2="0" y2="1">
          <stop offset="0" stop-color="#d04e4e"/>
          <stop offset="0.75" stop-color="#cc4a4b"/>
          <stop offset="1" stop-color="#a8302f"/>
        </linearGradient>
        <linearGradient id="bandPhoto" x1="0" y1="0" x2="0" y2="1">
          <stop offset="0" stop-color="#3a2a2a"/>
          <stop offset="0.55" stop-color="#1f1b1b"/>
          <stop offset="0.8" stop-color="#8e3a3a"/>
          <stop offset="1" stop-color="#d9c9c0"/>
        </linearGradient>
      </defs>
      <rect width="520" height="840" fill="url(#frontFade)"/>
      <polygon points="0,215 520,296 520,420 0,340" fill="var(--cream)" aria-hidden="true"/>
      <g role="img" aria-label="Grainy black-and-white photo of the five young Quillmarks with guitars and drumsticks, sitting on a fairground ride at Kite Pier, Hamburg 1960">
        <polygon points="0,330 120,300 520,330 520,640 0,585" fill="url(#bandPhoto)"/>
      </g>
      <polygon points="0,585 520,645 520,700 0,632" fill="var(--cream)" aria-hidden="true"/>
      <polygon points="0,680 520,745 520,790 0,722" fill="var(--cream)" aria-hidden="true"/>
    </svg>
    <h1 class="front-title">When <span class="accent">Sparrows</span><br>Quarrel</h1>
    <p class="novel-label">A Novel</p>
    <p class="author">BY MILO TAVISTRAND</p>
  </section>

</main>
</body>
</html>
```